Academy of Hops Business Card/Stamp card
Business card and stamp card
Creative Brief
Use specific fonts
Any font is fine.
Modern
Academy of Hops
2374 Larkwood Avenue Suite 410 Sacramento, CA 95816
NOmail@NOmailbox.example
www.TheZqm.example
The Largest Selection Of Craft Beers On Tap In All Of Sacramento! 100 on Tap
It will be a stamp card. Must contain all of this.... Collect 10 Stamps, and get one Zqm Bar Bite FREE Card must be stamped at the time of purchase. Stamps can be combined. Card(s) must be surrendered to receive a free Bar Bite. Not valid for employees and their relatives. Some restrictions may apply. Cannot be combined with any other offers. Not valid without coupon, or if reproduced. This offer can be canceled at anytime without notice.

```html
<!DOCTYPE html>
<html lang="en">
<head>
<meta charset="utf-8">
<title>Academy of Hops — Stationery and Stamp Card</title>
<link href="https://fonts.googleapis.com/css2?family=Montserrat:wght@400;600;700&family=Homemade+Apple&display=swap" rel="stylesheet">
<style>
:root{
  --bg:#e9eaec;
  --paper:#ffffff;
  --blue:#1f5a93;
  --gold:#c9962e;
  --ink:#4a4f57;
  --muted:#8a9099;
}
*{box-sizing:border-box;margin:0;padding:0}
html,body{width:1200px;height:937px;overflow:hidden}
body{background:var(--bg);font-family:"Montserrat",Arial,sans-serif;color:var(--ink);position:relative}
.sheet{position:absolute;background:var(--paper);overflow:hidden}
.sheet svg.edge{position:absolute;inset:0;width:100%;height:100%}
.brand{display:flex;flex-direction:column;align-items:center;gap:4px;font-weight:700;color:var(--blue);text-transform:uppercase;letter-spacing:.06em;text-align:center;position:absolute}
.brand .dot{border-radius:50%;background:var(--blue)}
/* letterhead */
.letterhead{left:182px;top:63px;width:408px;height:550px}
.letterhead .brand{left:34px;top:32px;width:86px;font-size:9px;line-height:1.15}
.letterhead .brand .dot{width:18px;height:18px}
.letter{position:absolute;left:34px;top:112px;width:280px;font-size:5.6px;line-height:1.6;color:var(--ink)}
.letter p{margin-bottom:8px}
.letter .sig{font-family:"Homemade Apple",cursive;font-size:12px;color:#333;margin:4px 0 2px}
.letter .footer{margin-top:26px;color:var(--muted);line-height:1.7}
/* folder */
.folder{left:633px;top:40px;width:390px;height:575px}
.folder .brand{left:60px;top:240px;width:250px;font-size:24px;line-height:1.1;gap:10px}
.folder .brand .dot{width:44px;height:44px}
/* business card */
.card{width:174px;height:102px}
.card-front{left:46px;top:653px}
.card-front .brand{left:8px;top:24px;width:56px;font-size:5.5px;line-height:1.1}
.card-front .brand .dot{width:12px;height:12px}
.card .contact{position:absolute;left:66px;top:14px;width:68px;font-size:4px;line-height:1.75;color:var(--ink)}
.card .contact strong{display:block;color:var(--blue);font-size:5.4px;margin-bottom:1px}
/* stamp card */
.stamp-card{left:46px;top:780px}
.stamp-card .brand{left:8px;top:8px;flex-direction:row;gap:4px;font-size:5.5px;line-height:1}
.stamp-card .brand .dot{width:9px;height:9px}
.stamp-card .tagline{position:absolute;left:8px;top:20px;width:128px;font-size:3.4px;font-weight:600;color:var(--gold);line-height:1.3}
.stamp-card .offer{position:absolute;left:8px;top:31px;width:128px;font-size:4.4px;font-weight:700;color:var(--blue);line-height:1.25}
.stamps{position:absolute;left:8px;top:44px;display:grid;grid-template-columns:repeat(5,12px);gap:3px 8px}
.stamps span{width:12px;height:12px;border-radius:50%;border:.8px solid var(--blue)}
.stamp-card .terms{position:absolute;left:8px;top:74px;width:128px;font-size:2.6px;line-height:1.3;color:var(--muted)}
/* envelopes */
.envelope{height:213px}
.envelope-front{left:263px;top:668px;width:433px}
.envelope-front .brand{left:18px;top:20px;width:70px;font-size:7px;line-height:1.1}
.envelope-front .brand .dot{width:14px;height:14px}
.envelope-back{left:739px;top:668px;width:421px}
.envelope-back .site{position:absolute;top:18px;right:40px;color:#fff;font-size:11px;letter-spacing:.14em}
</style>
</head>
<body>

<section class="sheet letterhead">
  <svg class="edge" viewBox="0 0 408 550" preserveAspectRatio="none">
    <path d="M362 0 Q320 300 336 550 L408 550 L408 0Z" fill="var(--blue)"/>
    <path d="M350 0 Q307 300 323 550" fill="none" stroke="var(--gold)" stroke-width="3"/>
  </svg>
  <div class="brand"><span class="dot"></span>Academy of Hops</div>
  <div class="letter">
    <p>June 12, 2024</p>
    <p>Jane Doe<br>Office Manager<br>120 Oak Street, Sacramento</p>
    <p>Dear Jane,</p>
    <p>Thank you for your visit last week. We are pleased to share our seasonal tap list and event calendar with your team. Please let us know if you have any questions about group bookings or private tastings.</p>
    <p>Our kitchen now serves a full bar bite menu until late every night, paired with rotating craft beers from local brewers.</p>
    <p>We look forward to welcoming you and your guests again soon.</p>
    <p>Kind regards,</p>
    <div class="sig">tovel</div>
    <p>Mark Tovel<br>Manager</p>
    <div class="footer">T: (916) 555-0142<br>2374 Larkwood Avenue Suite 410 Sacramento, CA 95816<br>NOmail@NOmailbox.example<br>www.TheZqm.example</div>
  </div>
</section>

<section class="sheet folder">
  <svg class="edge" viewBox="0 0 390 575" preserveAspectRatio="none">
    <path d="M350 0 Q322 300 345 575 L390 575 L390 0Z" fill="var(--blue)"/>
    <path d="M338 0 Q309 300 332 575" fill="none" stroke="var(--gold)" stroke-width="3"/>
  </svg>
  <div class="brand"><span class="dot"></span>Academy of Hops</div>
</section>

<section class="sheet card card-front">
  <svg class="edge" viewBox="0 0 174 102" preserveAspectRatio="none">
    <path d="M152 0 Q132 50 142 102 L174 102 L174 0Z" fill="var(--blue)"/>
    <path d="M147 0 Q127 50 137 102" fill="none" stroke="var(--gold)" stroke-width="1.2"/>
  </svg>
  <div class="brand"><span class="dot"></span>Academy of Hops</div>
  <div class="contact"><strong>Mark Tovel</strong>Manager<br>(916) 555-0142<br>NOmail@NOmailbox.example<br>www.TheZqm.example<br>2374 Larkwood Avenue Suite 410<br>Sacramento, CA 95816</div>
</section>

<section class="sheet card stamp-card">
  <svg class="edge" viewBox="0 0 174 102" preserveAspectRatio="none">
    <path d="M160 0 Q140 50 152 102 L174 102 L174 0Z" fill="var(--blue)"/>
    <path d="M155 0 Q135 50 147 102" fill="none" stroke="var(--gold)" stroke-width="1.2"/>
  </svg>
  <div class="brand"><span class="dot"></span>Academy of Hops</div>
  <p class="tagline">The Largest Selection Of Craft Beers On Tap In All Of Sacramento! 100 on Tap</p>
  <p class="offer">Collect 10 Stamps, and get one Zqm Bar Bite FREE</p>
  <div class="stamps"><span></span><span></span><span></span><span></span><span></span><span></span><span></span><span></span><span></span><span></span></div>
  <p class="terms">Card must be stamped at the time of purchase. Stamps can be combined. Card(s) must be surrendered to receive a free Bar Bite. Not valid for employees and their relatives. Some restrictions may apply. Cannot be combined with any other offers. Not valid without coupon, or if reproduced. This offer can be canceled at anytime without notice.</p>
</section>

<section class="sheet envelope envelope-front">
  <svg class="edge" viewBox="0 0 433 213" preserveAspectRatio="none">
    <path d="M376 0 Q352 110 368 213 L433 213 L433 0Z" fill="var(--blue)"/>
    <path d="M368 0 Q344 110 360 213" fill="none" stroke="var(--gold)" stroke-width="2"/>
  </svg>
  <div class="brand"><span class="dot"></span>Academy of Hops</div>
</section>

<section class="sheet envelope envelope-back">
  <svg class="edge" viewBox="0 0 421 213" preserveAspectRatio="none">
    <path d="M0 0 H421 V62 Q210 40 0 58Z" fill="var(--blue)"/>
    <path d="M0 63 Q210 45 421 67" fill="none" stroke="var(--gold)" stroke-width="2"/>
  </svg>
  <div class="site">www.TheZqm.example</div>
</section>

</body>
</html>
```